'TOLVANTA' NEW WINE LABEL DESIGN

I am looking for an exceptional and exciting design for a wine label called 'Tolvanta' meaning 'Lookout'. The design must feature the name 'Tolvanta', and the word 'Cabernet Sauvignon' in version 1 and 'Sauvignon Blanc' in version 2. It will also need the words 'Valle Central, Chile' at the bottom of the label as a prominent piece of information as well as the vintage 2017. Please produce the work in size 80mm x 100mm. Feel free to use colour in addition to black/white and ensue that the label is easy to read on a shelf placement.
Target Market(s)
SUPERMARKETS & WINE STORES
Requirements
Must have
- EASY TO READ, USE COLOURS LIKE GREEN FOR SAUVIGNON & RED FOR CABERNET SAUVIGNON
- FULL BOTTLE SHOT MUST BE IN PROVIDED DESIGNS. ALL BOTTLE TOPS SHOULD BE QUORLAN STYLE (SCREW TOP)
- PLEASE NOTE THAT LABEL INFORMATION MUSY BE EASY TO READ I.E. VINTAGE, PLACE OF ORGIN ALTHOUGH NOT THE MAIN CONTENT MUST STILL BE CLEAR.
Nice to have
- ARTISTIC REFERENCE LINK TO NAME & ANDES BUT NOT PICTURES OF MOUNTAINS
Should not have
- PICTURES OF GRAPES
- PICTURES OF VINEYARDS
- PICTURES OF MOUNTAINS

```html
<!DOCTYPE html>
<html lang="en">
<head>
<meta charset="utf-8">
<title>Tolvanta Sauvignon Blanc – Label</title>
<link rel="stylesheet" href="https://fonts.googleapis.com/css2?family=Cinzel:wght@500&family=Lato:wght@700&family=Pinyon+Script&display=swap">
<style>
  :root {
    --backdrop: #f4f4f2;
    --paper: #e9e7e8;
    --ink: #1d1d1d;
    --gold: #9a7440;
    --rule: #9a9898;
    --leaf-light: #c9dc5a;
    --leaf-mid: #7fbf4a;
    --leaf-deep: #3f8a5a;
    --bronze: #6b4a22;
  }
  * { margin: 0; padding: 0; box-sizing: border-box; }
  html, body {
    width: 1200px; height: 1200px; overflow: hidden;
    background: var(--backdrop);
  }
  .canvas {
    width: 1200px; height: 1200px;
    display: flex; align-items: center; justify-content: center;
  }
  .label {
    position: relative;
    width: 880px; height: 1100px;
    background: var(--paper);
    box-shadow: 0 2px 14px rgba(0,0,0,0.08);
    display: flex; flex-direction: column; align-items: center;
  }
  .label__artwork {
    margin-top: 190px;
    width: 760px; height: 260px;
  }
  .label__brand {
    margin-top: 40px;
    font-family: "Cinzel", serif;
    font-weight: 500;
    font-size: 118px;
    letter-spacing: 0.08em;
    color: var(--ink);
    line-height: 1;
  }
  .label__rule {
    margin-top: 42px;
    width: 140px; height: 2px;
    background: var(--rule);
  }
  .label__varietal {
    margin-top: 34px;
    font-family: "Lato", sans-serif;
    font-weight: 700;
    font-size: 30px;
    letter-spacing: 0.22em;
    color: var(--gold);
    font-variant: small-caps;
    text-transform: lowercase;
  }
  .label__varietal .cap { text-transform: uppercase; font-size: 40px; }
  .label__origin {
    margin-top: 8px;
    font-family: "Pinyon Script", cursive;
    font-size: 68px;
    color: var(--ink);
    line-height: 1.2;
  }
  .label__vintage {
    margin-top: 6px;
    font-family: "Lato", sans-serif;
    font-weight: 700;
    font-size: 34px;
    letter-spacing: 0.22em;
    color: var(--gold);
  }
</style>
</head>
<body>
  <main class="canvas">
    <article class="label">
      <svg class="label__artwork" viewBox="0 0 760 260" role="img" aria-label="Watercolour landscape artwork in yellow-green, green and bronze brushstrokes">
        <defs>
          <linearGradient id="artwork-wash" x1="0" y1="0" x2="1" y2="0">
            <stop offset="0" stop-color="var(--leaf-light)" stop-opacity="0"/>
            <stop offset="0.2" stop-color="var(--leaf-light)" stop-opacity="0.8"/>
            <stop offset="0.5" stop-color="var(--leaf-mid)" stop-opacity="0.85"/>
            <stop offset="0.75" stop-color="var(--leaf-deep)" stop-opacity="0.8"/>
            <stop offset="1" stop-color="var(--bronze)" stop-opacity="0.9"/>
          </linearGradient>
          <filter id="soft-edge"><feGaussianBlur stdDeviation="14"/></filter>
        </defs>
        <ellipse cx="400" cy="140" rx="340" ry="80" fill="url(#artwork-wash)" filter="url(#soft-edge)"/>
      </svg>
      <h1 class="label__brand">TOLVANTA</h1>
      <div class="label__rule"></div>
      <p class="label__varietal"><span class="cap">S</span>auvignon <span class="cap">B</span>lanc</p>
      <p class="label__origin">Valle Central, Chile</p>
      <p class="label__vintage">2017</p>
    </article>
  </main>
</body>
</html>
```